New Business Card Design Project

Hi! We require a design for business cards for directors and head teachers of an international daycare for children 0 - 9. We are family-owned, -operated and -oriented. We have six locations, looking to franchise. Our USPs are: 1) Flexibility 2) Quality teachers 3) International culture 4) Best nutrition We are quality teachers and professional caretakers, but with creativity and personality! Business cards should be playful (but no Comic Sans or baby hand prints), colorful (but no rainbows), and have some breathing space. It should be obvious from the business card that we're a daycare. In 2020 we'll be launching our new website based on this design: https://plinvo.example/47K2RTWZMPD The font in the new website will be Houschka (medium, demibold, bold). We will keep our current logo, included in the files here. There are also screenshots of some designs we like. Show us your best! :)

Industry/Entity Type

Childcare

Contact Information for Business Card

Femke de Lorre
Communications Wizard
Pluma Tots International Daycare
Voskuilstraat 47 B, 2345 KR Leiden
www.plumatots.example
+31 647153826

Font styles to use
Serif
Sans Serif

Colors

Designer to choose colors to be used in the design.

Requirements
Must have
• Color

```html
<!DOCTYPE html>
<html lang="en">
<head>
<meta charset="utf-8">
<title>Pluma Tots – Business Card</title>
<link href="https://fonts.googleapis.com/css2?family=Quicksand:wght@500;600;700&display=swap" rel="stylesheet">
<style>
  :root {
    --pink: #e94c80;
    --blue: #14ade0;
    --white: #ffffff;
    --grey-text: #6d6d6d;
    --page: #e9eaee;
  }
  * { box-sizing: border-box; margin: 0; padding: 0; }
  html, body {
    width: 1200px; height: 1000px; overflow: hidden;
    background: var(--page);
    font-family: "Quicksand", sans-serif;
  }
  .sheet {
    width: 1200px; height: 1000px;
    display: flex; flex-direction: column; align-items: center; justify-content: center;
    gap: 40px;
  }
  .card {
    position: relative;
    width: 760px; height: 440px;
    border-radius: 26px;
    overflow: hidden;
    box-shadow: 0 10px 30px rgba(0,0,0,0.15);
  }
  /* Front */
  .card--front {
    background: var(--pink);
    display: flex; align-items: center; justify-content: center;
  }
  .brand {
    display: flex; align-items: center; gap: 16px;
    font-weight: 700; color: var(--white);
  }
  .brand__dot { width: 34px; height: 34px; border-radius: 50%; background: var(--white); }
  .brand__name { font-size: 64px; letter-spacing: 1px; }

  /* Back */
  .card--back { background: var(--white); }
  .card--back .brand { position: absolute; left: 56px; top: 70px; color: var(--pink); }
  .card--back .brand__dot { width: 24px; height: 24px; background: var(--blue); }
  .card--back .brand__name { font-size: 44px; }

  .divider {
    position: absolute; left: 44px; right: 56px; top: 236px;
    height: 2px; background: var(--pink);
  }
  .person {
    position: absolute; right: 70px; top: 150px; text-align: right;
  }
  .person__name { font-size: 30px; font-weight: 700; color: var(--pink); }
  .person__name .accent { color: var(--blue); }
  .person__role { font-size: 19px; font-weight: 500; color: var(--grey-text); margin-top: 2px; letter-spacing: 0.5px; }
  .edge-tab {
    position: absolute; right: 0; top: 150px; width: 16px; height: 66px; background: var(--pink);
  }
  .contacts {
    position: absolute; left: 52px; top: 262px; list-style: none;
    font-size: 18px; font-weight: 500; color: var(--grey-text); letter-spacing: 0.4px;
  }
  .contacts li { display: flex; align-items: center; gap: 10px; line-height: 30px; }
  .contacts svg { width: 16px; height: 16px; fill: var(--pink); flex: none; }
  .address {
    position: absolute; right: 70px; top: 296px; text-align: right;
    font-size: 19px; font-weight: 500; color: var(--grey-text); line-height: 28px; letter-spacing: 0.4px;
  }
  .bottom-band { position: absolute; left: 0; bottom: 0; width: 100%; height: 20px; }
</style>
</head>
<body>
<main class="sheet">
  <section class="card card--front">
    <div class="brand"><span class="brand__dot"></span><span class="brand__name">Pluma Tots</span></div>
  </section>

  <section class="card card--back">
    <div class="brand"><span class="brand__dot"></span><span class="brand__name">Pluma Tots</span></div>

    <div class="person">
      <p class="person__name">Femke de <span class="accent">Lorre</span></p>
      <p class="person__role">Communications Wizard</p>
    </div>
    <span class="edge-tab"></span>

    <div class="divider"></div>

    <ul class="contacts">
      <li>
        <svg viewBox="0 0 24 24"><path d="M6.6 10.8a15 15 0 0 0 6.6 6.6l2.2-2.2a1 1 0 0 1 1-.25 11.4 11.4 0 0 0 3.6.57 1 1 0 0 1 1 1V20a1 1 0 0 1-1 1A17 17 0 0 1 3 4a1 1 0 0 1 1-1h3.5a1 1 0 0 1 1 1c0 1.25.2 2.45.57 3.57a1 1 0 0 1-.25 1z"/></svg>
        +31 647153826
      </li>
      <li>
        <svg viewBox="0 0 24 24"><path d="M2 5h20v14H2z M4 7v.5l8 5 8-5V7l-8 5z" fill-rule="evenodd"/></svg>
        info@plumatots.example
      </li>
      <li>
        <svg viewBox="0 0 24 24"><circle cx="12" cy="12" r="10"/></svg>
        www.plumatots.example
      </li>
    </ul>

    <div class="address">
      <p>Pluma Tots International Daycare</p>
      <p>Voskuilstraat 47 B, 2345 KR Leiden</p>
    </div>

    <svg class="bottom-band" viewBox="0 0 760 20" preserveAspectRatio="none">
      <polygon points="0,0 350,0 330,20 0,20" fill="var(--blue)"/>
      <polygon points="362,0 760,0 760,20 342,20" fill="var(--pink)"/>
    </svg>
  </section>
</main>
</body>
</html>
```